Business Card Design for a Sound engineer and DJ

We would like a residn of the business card.

Logo must remain the same.
The card is for the owner of the company.
The business card is in Arabic as the company is based in Kuwait.
The company specializes in sound engineering for singers concerts and events and in addition DJ.
The color options is up to the designer but we would like it masculine as the owner is a man.

Target Market(s)

All ages

Industry/Entity Type

Media

Contact Information for Business Card

Name:
Eng. Tarek Halabi
م/طارق حلبي

The name above is in Arabic and English.

Title: General Manager
Mobile: +965 66307852
Office: +965 22486037
Email: info@sawtarin.net

Address:
Office no. 3
1st floor
Almarfa Complex
Rashed AlQeblawi St.
Salmiya
Kuwait

Instagram: @sawtarin
Snap: sawtarin

Requirements
Nice to have
• can we have Instagram icon and snap icon and a phone vector and email?
• Instead of writing the words

```html
<!DOCTYPE html>
<html lang="en">
<head>
<meta charset="utf-8">
<title>Sawtarin – Business Card</title>
<link rel="stylesheet" href="https://fonts.googleapis.com/css2?family=Open+Sans:wght@400;600;700&family=Noto+Sans+Arabic:wght@500;700&display=swap">
<style>
  :root {
    --page: #e9e6e2;
    --card: #ffffff;
    --magenta: #b0368f;
    --purple: #7a4fa3;
    --violet: #8a5cb8;
    --ink: #3a3a3a;
    --band-a: #6f7fc4;
    --band-b: #b9c2ea;
  }
  * { box-sizing: border-box; margin: 0; padding: 0; }
  html, body { width: 1200px; height: 843px; overflow: hidden; }
  body {
    background: var(--page);
    font-family: "Open Sans", Arial, sans-serif;
    color: var(--ink);
    position: relative;
  }
  .card {
    position: absolute;
    width: 660px; height: 377px;
    background: var(--card);
    box-shadow: 0 12px 30px rgba(0,0,0,.22);
    overflow: hidden;
  }
  .card-back { left: 60px; top: 28px; }
  .card-front { left: 480px; top: 436px; }

  /* back side */
  .social { position: absolute; right: 24px; top: 18px; display: flex; align-items: center; gap: 7px;
    font-size: 13px; font-weight: 600; color: var(--purple); }
  .social-dot { width: 14px; height: 14px; border-radius: 50%; background: var(--purple); }
  .back-brand { position: absolute; left: 0; right: 0; top: 128px; text-align: center; }
  .back-brand-row { display: inline-flex; align-items: center; gap: 14px; }
  .brand-square { width: 34px; height: 34px; background: var(--violet); }
  .back-brand-name { font-size: 40px; font-weight: 400; color: var(--violet); line-height: 1; }
  .back-tag { font-size: 12px; font-weight: 600; color: var(--violet); letter-spacing: 2px; margin-top: 12px; }
  .back-tag-ar { font-family: "Noto Sans Arabic", "Open Sans", sans-serif; font-size: 15px; font-weight: 500;
    color: var(--violet); direction: rtl; margin-top: 2px; }

  /* front side */
  .holder { position: absolute; left: 36px; top: 22px; }
  .holder-name { font-size: 23px; font-weight: 700; color: var(--magenta); line-height: 1.15; }
  .holder-name-ar { font-family: "Noto Sans Arabic", "Open Sans", sans-serif; font-size: 18px; font-weight: 700;
    color: var(--magenta); direction: rtl; text-align: left; line-height: 1.35; }
  .holder-title { font-size: 14px; margin-top: 4px; }
  .address { position: absolute; left: 36px; top: 128px; font-size: 14px; line-height: 1.35; font-style: normal; }
  .contacts { position: absolute; left: 32px; top: 218px; list-style: none; font-size: 14px; line-height: 1.55; }
  .contacts li { display: flex; align-items: center; gap: 8px; }
  .contacts svg { width: 13px; height: 13px; fill: var(--purple); flex: none; }
  .brand { position: absolute; right: 34px; top: 30px; text-align: right; }
  .brand-name { font-size: 32px; font-weight: 400; color: var(--violet); line-height: 1; }
  .brand-tag { font-size: 10px; font-weight: 600; color: var(--violet); letter-spacing: 2px; margin-top: 6px; }
  .brand-tag-ar { font-family: "Noto Sans Arabic", "Open Sans", sans-serif; font-size: 13px; font-weight: 500;
    color: var(--violet); direction: rtl; }
  .equalizer-art { position: absolute; left: 270px; top: 150px; width: 360px; height: 227px; }
  .bottom-band { position: absolute; left: 0; bottom: 0; width: 660px; height: 72px; }
</style>
</head>
<body>
  <div class="card card-back">
    <div class="social"><span class="social-dot"></span>@sawtarin</div>
    <section class="back-brand">
      <div class="back-brand-row">
        <span class="brand-square"></span>
        <p class="back-brand-name">Sawtarin</p>
      </div>
      <p class="back-tag">DJ - SOUND ENG. - LIGHTING</p>
      <p class="back-tag-ar">دي جي - هندسة صوت - إضاءة</p>
    </section>
  </div>

  <div class="card card-front">
    <svg class="bottom-band" viewBox="0 0 660 72" preserveAspectRatio="none">
      <defs>
        <linearGradient id="bandFill" x1="0" y1="0" x2="1" y2="0">
          <stop offset="0" stop-color="var(--band-a)"/>
          <stop offset="1" stop-color="var(--band-b)"/>
        </linearGradient>
      </defs>
      <path d="M0 10 Q330 46 660 54 L660 72 L0 72 Z" fill="url(#bandFill)"/>
    </svg>

    <svg class="equalizer-art" role="img" aria-label="Decorative sound equalizer bars with music notes" viewBox="0 0 360 227">
      <defs>
        <linearGradient id="eqFill" x1="0" y1="1" x2="1" y2="0">
          <stop offset="0" stop-color="#9a86c8" stop-opacity=".5"/>
          <stop offset=".6" stop-color="#a04fa8" stop-opacity=".5"/>
          <stop offset="1" stop-color="#e0408f" stop-opacity=".55"/>
        </linearGradient>
      </defs>
      <rect x="0" y="0" width="360" height="227" rx="4" fill="url(#eqFill)"/>
    </svg>

    <section class="holder">
      <h1 class="holder-name">Tarek Halabi</h1>
      <p class="holder-name-ar">م/طارق حلبي</p>
      <p class="holder-title">General Manager</p>
    </section>

    <address class="address">
      Office no. 3, 1st floor<br>
      Almarfa Complex<br>
      Rashed AlQeblawi St.<br>
      Salmiya, Kuwait
    </address>

    <ul class="contacts">
      <li><svg viewBox="0 0 20 20"><rect x="5" y="1" width="10" height="18" rx="2"/><rect x="7" y="3" width="6" height="11" fill="#fff"/></svg>+965 66307852</li>
      <li><svg viewBox="0 0 20 20"><path d="M4 2l4 1 1 4-2 2c1 2 3 4 5 5l2-2 4 1 0 4c-8 1-15-6-14-15z"/></svg>+965 22486037</li>
      <li><svg viewBox="0 0 20 20"><rect x="1" y="4" width="18" height="12" rx="1"/><path d="M2 5l8 6 8-6" stroke="#fff" stroke-width="1.6" fill="none"/></svg>info@sawtarin.net</li>
      <li><svg viewBox="0 0 20 20"><circle cx="10" cy="10" r="9"/><path d="M1 10h18M10 1c-4 5-4 13 0 18M10 1c4 5 4 13 0 18" stroke="#fff" stroke-width="1.3" fill="none"/></svg>www.sawtarin.net</li>
    </ul>

    <section class="brand">
      <p class="brand-name">Sawtarin</p>
      <p class="brand-tag">DJ - SOUND ENG. - LIGHTING</p>
      <p class="brand-tag-ar">دي جي - هندسة صوت - إضاءة</p>
    </section>
  </div>
</body>
</html>
```